A new presentation to our clients

we are a Real Estate agency, our website is www.dorelumia.com and it’s time to have a new, fashion and remarcable Business Card. we want to differentiate ourselves from other companies so we want a business card that differentiates us. we want the business card to impact our customers. in the competitive market that we have today, we have to be different and it is this difference that we seek

Target Market(s)

Real Estate Clients

Contact Information for Business Card

We search a totaly diferent card from the usual

Font styles to use
Sans Serif

Colors
e34197

Requirements
Must have
• Logo, adress, phone contact, e-mail, photo, and our website
Nice to have
• We would like to see a modern business card
Should not have
• Houses or building draws

```html
<!DOCTYPE html>
<html lang="en">
<head>
<meta charset="utf-8">
<title>Dore Lumia – Business Card</title>
<link rel="stylesheet" href="https://fonts.googleapis.com/css2?family=Arimo:wght@400;700&display=swap">
<style>
  :root {
    --backdrop: #2a2a2c;
    --card-white: #f4f4f4;
    --card-dark: #232224;
    --brand-pink: #d61a6e;
    --strip-pink: #b8185f;
    --text-light: #e6e6e6;
    --tagline-text: #f6e3ec;
  }
  * { box-sizing: border-box; margin: 0; padding: 0; }
  html, body { width: 1200px; height: 997px; overflow: hidden; }
  body {
    background: var(--backdrop);
    font-family: "Arimo", Arial, sans-serif;
    position: relative;
  }
  .business-card {
    position: absolute;
    left: 180px; top: 258px;
    width: 840px; height: 480px;
    border-radius: 70px 0 70px 0;
    overflow: hidden;
    background: var(--card-dark);
    box-shadow: 0 18px 40px rgba(0,0,0,.55);
  }
  .card-header {
    position: absolute; left: 0; top: 0;
    width: 100%; height: 195px;
    background: var(--card-white);
    display: flex; align-items: center; justify-content: center;
  }
  .brand-name {
    font-weight: 700;
    font-size: 88px;
    color: var(--brand-pink);
    letter-spacing: 1px;
  }
  .contact-block {
    position: absolute; left: 40px; top: 212px;
    color: var(--text-light);
  }
  .person-name {
    font-weight: 700; font-size: 20px; line-height: 23px;
    color: var(--brand-pink); letter-spacing: 1px;
    text-transform: uppercase;
  }
  .person-role { font-size: 16px; line-height: 18px; margin-top: 3px; }
  .address { font-size: 16px; line-height: 20px; margin-top: 14px; }
  .contact-list { list-style: none; margin-top: 10px; }
  .contact-item {
    display: flex; align-items: center; gap: 12px;
    font-size: 17px; height: 25px;
  }
  .contact-icon { width: 20px; height: 20px; flex: none; }
  .website {
    position: absolute; right: 40px; top: 390px;
    font-size: 18px; font-weight: 700;
    color: var(--brand-pink);
  }
  .tagline-strip {
    position: absolute; left: 0; bottom: 0;
    width: 100%; height: 55px;
    background: var(--strip-pink);
    display: flex; align-items: center; justify-content: center;
  }
  .tagline {
    color: var(--tagline-text); font-weight: 700; font-size: 18px;
    letter-spacing: 4px; text-transform: uppercase;
  }
</style>
</head>
<body>
  <main class="business-card">
    <header class="card-header">
      <span class="brand-name">Dore Lumia</span>
    </header>

    <section class="contact-block">
      <p class="person-name">Marco T. Feliciano</p>
      <p class="person-role">Business Adviser</p>
      <p class="address">Rua das Flores Altas, 118<br>4050-262, Porto Norte</p>
      <ul class="contact-list">
        <li class="contact-item">
          <svg class="contact-icon" viewBox="0 0 20 20" aria-hidden="true">
            <circle cx="10" cy="10" r="10" fill="var(--brand-pink)"/>
            <path d="M6 6.5c0 4 3.5 7.5 7.5 7.5l1-1.8-2.2-1-1 1c-1.5-.6-2.9-2-3.5-3.5l1-1-1-2.2z" fill="#fff"/>
          </svg>
          555-014-2281
        </li>
        <li class="contact-item">
          <svg class="contact-icon" viewBox="0 0 20 20" aria-hidden="true">
            <circle cx="10" cy="10" r="10" fill="var(--brand-pink)"/>
            <rect x="5" y="6.5" width="10" height="7" fill="none" stroke="#fff" stroke-width="1.3"/>
            <path d="M5 6.5l5 4 5-4" fill="none" stroke="#fff" stroke-width="1.3"/>
          </svg>
          555-016-7390
        </li>
        <li class="contact-item">
          <svg class="contact-icon" viewBox="0 0 20 20" aria-hidden="true">
            <circle cx="10" cy="10" r="10" fill="var(--brand-pink)"/>
            <path d="M8.5 11.5l3-3M9 7l1-1a2 2 0 013 3l-1 1M11 13l-1 1a2 2 0 01-3-3l1-1" fill="none" stroke="#fff" stroke-width="1.3" stroke-linecap="round"/>
          </svg>
          marco@dorelumia.com
        </li>
      </ul>
    </section>

    <p class="website">www.dorelumia.com</p>

    <footer class="tagline-strip">
      <span class="tagline">Houses, Apartments, Real Estate, Trade</span>
    </footer>
  </main>
</body>
</html>
```